Business Card Design Project

Small privately owned salon.

Industry/Entity Type

Business

Contact Information for Business Card

Hair salon.i would like my logo to be my name , Marisol Denby. Address and phone can go on the front or back. The back will be where I write their appt.
address-362 Thistledown lane York, Pa. 17488
Phone- 717-555-0148

```html
<!DOCTYPE html>
<html lang="en">
<head>
<meta charset="utf-8">
<title>Marisol Denby Hair Salon – Business Card</title>
<link rel="stylesheet" href="https://fonts.googleapis.com/css2?family=Poiret+One&family=Questrial&family=Tinos&display=swap">
<style>
  :root {
    --backdrop: #d6d6d6;
    --card-white: #ffffff;
    --card-dark: #2b2a29;
    --ink: #2b2a29;
    --ink-light: #ffffff;
    --gold-light: #f3d99a;
    --gold: #c9a24e;
    --gold-dark: #8a6a25;
    --rule: #2b2a29;
  }
  * { box-sizing: border-box; margin: 0; padding: 0; }
  html, body {
    width: 1100px;
    height: 1200px;
    overflow: hidden;
    background: var(--backdrop);
  }
  .canvas {
    position: relative;
    width: 1100px;
    height: 1200px;
  }
  .card {
    position: absolute;
    left: 159px;
    width: 767px;
    height: 427px;
    border-radius: 32px;
    overflow: hidden;
    background: var(--card-white);
    box-shadow: 0 4px 10px rgba(0,0,0,0.18);
  }
  .card--appointment { top: 128px; }
  .card--identity { top: 628px; }

  /* Appointment side */
  .side-panel {
    position: absolute;
    left: 0; top: 0;
    width: 171px;
    height: 100%;
    background: var(--card-dark);
  }
  .gold-twist {
    background: linear-gradient(90deg, var(--gold-dark), var(--gold-light) 45%, var(--gold) 70%, var(--gold-dark));
  }
  .gold-twist--vertical {
    position: absolute;
    left: 160px; top: 0;
    width: 22px;
    height: 100%;
  }
  .appointment-form {
    position: absolute;
    left: 224px;
    top: 96px;
    font-family: "Questrial", sans-serif;
    font-size: 24px;
    color: var(--ink);
  }
  .appointment-form .heading { margin-bottom: 58px; }
  .field {
    display: flex;
    align-items: flex-end;
    height: 32px;
    margin-bottom: 58px;
  }
  .field .label { margin-right: 10px; }
  .field .line {
    border-bottom: 1.5px solid var(--rule);
    height: 24px;
  }
  .field--date .line { width: 400px; }
  .field--time .line { width: 400px; }

  /* Identity side */
  .identity-band {
    position: absolute;
    left: 0; top: 236px;
    width: 100%;
    height: 191px;
    background: var(--card-dark);
  }
  .salon-name {
    position: absolute;
    left: 0; top: 140px;
    width: 100%;
    text-align: center;
    font-family: "Poiret One", sans-serif;
    font-size: 56px;
    color: var(--ink);
    letter-spacing: 1px;
  }
  .gold-twist--horizontal {
    position: absolute;
    left: 187px; top: 228px;
    width: 390px;
    height: 20px;
    border-radius: 10px;
    background: linear-gradient(180deg, var(--gold-light), var(--gold) 50%, var(--gold-dark));
  }
  .salon-tagline {
    position: absolute;
    left: 187px; top: 256px;
    width: 390px;
    text-align: center;
    font-family: "Questrial", sans-serif;
    font-size: 25px;
    letter-spacing: 17px;
    padding-left: 17px;
    color: var(--ink-light);
  }
  .contact {
    position: absolute;
    left: 0; top: 330px;
    width: 100%;
    display: flex;
    justify-content: center;
    gap: 36px;
    font-family: "Tinos", serif;
    font-size: 25px;
    color: var(--ink-light);
  }
  .contact-item {
    display: flex;
    align-items: center;
    gap: 6px;
  }
  .contact-item svg { display: block; }
</style>
</head>
<body>
<main class="canvas">

  <section class="card card--appointment" aria-label="Appointment card, back">
    <div class="side-panel"></div>
    <div class="gold-twist gold-twist--vertical" role="img" aria-label="Twisted gold ribbon border"></div>
    <div class="appointment-form">
      <p class="heading">Next appointment:</p>
      <div class="field field--date"><span class="label">Date</span><span class="line"></span></div>
      <div class="field field--time"><span class="label">Time</span><span class="line"></span></div>
    </div>
  </section>

  <section class="card card--identity" aria-label="Business card, front">
    <h1 class="salon-name">Marisol Denby</h1>
    <div class="identity-band"></div>
    <div class="gold-twist--horizontal" role="img" aria-label="Twisted gold ribbon divider"></div>
    <p class="salon-tagline">HAIR SALON</p>
    <div class="contact">
      <span class="contact-item">
        <svg width="18" height="28" viewBox="0 0 18 28" aria-hidden="true">
          <path d="M9 1C4.6 1 1 4.5 1 8.9 1 15 9 27 9 27s8-12 8-18.1C17 4.5 13.4 1 9 1z" fill="#c9a24e"/>
          <circle cx="9" cy="9" r="3.2" fill="#2b2a29"/>
        </svg>
        362 Thistledown lane York, Pa. 17488
      </span>
      <span class="contact-item">
        <svg width="18" height="24" viewBox="0 0 18 24" aria-hidden="true">
          <path d="M5 2l3 5-2 2c1 3 3 6 6 8l2-2 4 3-2 4C9 21 2 13 1 5z" fill="#c9a24e"/>
        </svg>
        717-555-0148
      </span>
    </div>
  </section>

</main>
</body>
</html>
```